The Front Porch Playbook

I have a book that I need a cover for. The main title will be "The Greenvale Front Porch Playbook" and the secondary title will be "12 lessons from an open door" With the design, I think I'd like to include some sort of blueprint drawing with drafting like font. But the blueprint drawing isn't a requirement.

Target Market(s)

Home/property sellers

Industry/Entity Type

Real Estate

Font styles to use
Serif
Sans Serif
Other font styles liked:
• Architect type handwriting

```html
<!DOCTYPE html>
<html lang="en">
<head>
<meta charset="utf-8">
<title>The Greenvale Front Porch Playbook – Book Cover</title>
<link rel="stylesheet" href="https://fonts.googleapis.com/css2?family=EB+Garamond&family=Old+Standard+TT:wght@400;700&family=Oswald:wght@300;500&display=swap">
<style>
  :root {
    --cover-blue: #2f5fdc;
    --spine-blue: #3b6ff0;
    --ink-white: #ffffff;
    --tagline-blue: #1d5aa6;
    --photo-light: #eef1f3;
    --photo-mid: #d9dde2;
    --photo-warm: #b5533a;
    --photo-wood: #8a5a3a;
  }
  html, body {
    margin: 0;
    padding: 0;
    width: 1200px;
    height: 864px;
    overflow: hidden;
    background: #ffffff;
  }
  .cover {
    position: relative;
    width: 1200px;
    height: 864px;
    background: var(--cover-blue);
    overflow: hidden;
    color: var(--ink-white);
  }
  .back {
    position: absolute;
    left: 0; top: 0;
    width: 574px; height: 864px;
  }
  .back-copy {
    position: absolute;
    left: 57px; top: 58px;
    width: 466px;
    font-family: "EB Garamond", serif;
    font-size: 20.5px;
    line-height: 22.4px;
    text-align: justify;
    hyphens: auto;
  }
  .back-copy p { margin: 0 0 22.4px; }
  .barcode-space {
    position: absolute;
    left: 372px; top: 717px;
    width: 147px; height: 115px;
    background: var(--ink-white);
  }
  .spine {
    position: absolute;
    left: 574px; top: 0;
    width: 50px; height: 864px;
    background: var(--spine-blue);
  }
  .spine-author, .spine-title {
    position: absolute;
    left: 50%;
    white-space: nowrap;
    transform-origin: center;
  }
  .spine-author {
    top: 160px;
    font-family: "Oswald", sans-serif;
    font-weight: 300;
    font-size: 19px;
    letter-spacing: 9px;
    transform: translate(-50%, -50%) rotate(-90deg);
  }
  .spine-title {
    top: 574px;
    font-family: "Old Standard TT", serif;
    font-size: 28px;
    transform: translate(-50%, -50%) rotate(-90deg);
  }
  .front {
    position: absolute;
    left: 624px; top: 0;
    width: 576px; height: 864px;
    overflow: hidden;
  }
  .front-author {
    position: absolute;
    left: 0; right: 0; top: 14px;
    text-align: center;
    font-family: "Oswald", sans-serif;
    font-weight: 300;
    font-size: 44px;
    letter-spacing: 21px;
    padding-left: 21px;
  }
  .title {
    position: absolute;
    left: 0; right: 0; top: 92px;
    text-align: center;
    font-family: "Old Standard TT", serif;
    font-weight: 700;
    line-height: 1;
    margin: 0;
  }
  .title .title-lead { display: block; font-size: 48px; margin-left: 30px; }
  .title .title-place { display: block; font-size: 92px; margin-top: -8px; letter-spacing: -2px; }
  .title .title-main { display: block; font-size: 42px; margin-top: 2px; }
  .photo {
    position: absolute;
    left: 0; top: 0;
  }
  .tagline {
    position: absolute;
    left: 284px; top: 356px;
    width: 276px;
    font-family: "Oswald", sans-serif;
    font-weight: 500;
    font-size: 21px;
    line-height: 1;
    color: var(--tagline-blue);
    text-transform: uppercase;
    white-space: nowrap;
    transform: rotate(7.5deg);
    transform-origin: left center;
  }
</style>
</head>
<body>
<div class="cover">
  <section class="back">
    <div class="back-copy">
      <p>Lorem ipsum dolor sit amet, consectetur adipiscing elit. Etiam faucibus tortor eget aliquam fringilla. Maecenas eget elit vitae ex imperdiet finibus nec quis ex. Vestibulum ante ipsum primis in faucibus orci luctus et ultrices posuere cubilia Curae; Morbi ut iaculis tortor. Interdum et malesuada fames ac ante ipsum primis in faucibus. Donec id malesuada orci. Aliquam fermentum rutrum scelerisque. In euismod tempor urna, nec tristique sem mattis nec. Aliquam vel dignissim quam.</p>
      <p>Sed viverra quis neque vel varius. Etiam vel pulvinar nulla. Proin sagittis nulla non nisl vehicula, quis sagittis augue consectetur. Vestibulum eget nulla ac neque pulvinar pharetra. Sed lacinia malesuada neque, sagittis finibus odio ornare ut. Vivamus ultricies ipsum nec risus rhoncus vulputate. Aenean tincidunt sit amet odio ac vehicula. Nulla nulla ante, fringilla a facilisis et, aliquet sed purus. Nunc luctus sapien ipsum, sed varius mauris fermentum a. Duis nec risus elementum, aliquet ligula vel, efficitur nibh. Nunc et felis sed leo imperdiet ultrices.</p>
    </div>
    <div class="barcode-space"></div>
  </section>

  <section class="spine">
    <div class="spine-author">AUTHOR NAME</div>
    <div class="spine-title">The Greenvale Front Porch Playbook</div>
  </section>

  <section class="front">
    <svg class="photo" width="576" height="864" viewBox="0 0 576 864" role="img" aria-label="Photo of a small model house with a red brick front and grey roof standing on blueprint plans beside a set of house keys">
      <defs>
        <linearGradient id="photoTone" x1="0" y1="0" x2="1" y2="1">
          <stop offset="0" stop-color="#8a5a3a"/>
          <stop offset="0.25" stop-color="#b5533a"/>
          <stop offset="0.55" stop-color="#d9dde2"/>
          <stop offset="1" stop-color="#eef1f3"/>
        </linearGradient>
      </defs>
      <polygon points="0,304 576,384 576,864 0,864" fill="url(#photoTone)"/>
    </svg>

    <div class="front-author">AUTHOR NAME</div>
    <h1 class="title">
      <span class="title-lead">The</span>
      <span class="title-place">Greenvale</span>
      <span class="title-main">Front Porch Playbook</span>
    </h1>
    <div class="tagline">12 lessons from an open door</div>
  </section>
</div>
</body>
</html>
```